Church Website with Home Page and Member Sermon Library

I am in need of an updated design for our church website. This will include 4 pages (outlined below). We are a conservative, evangelical, Christian church. The site should be modern and clean, while still reflecting our conservative values. I already have a logo for our church, and I want the site to incorporate the logo, and match the logo/branding. Stock photos are allowed if needed, but I have uploaded some images of our church and would prefer those images to be used if possible. Any stock photos used should not include any people in the photos (scenery, nature, buildings, animals, etc. are fine).

The site will need 4 pages: Home, Support Us (Donate), Login, and Recording Library.

Page 1: Home
The home page should include the following sections:

- Navigation: Should include links to each section of the home page plus a "listen live" link which will take the user to a live-streaming site and a "support us" link which will take the user to a support/donate page.

- Announcements: Can be either a banner or some other design, but there needs to be some way for us to post announcements for visitors to see. I'm open for creative ideas in this section, but would like it not to take up a lot of room on the page.

- About Us: Should include address, service times (see attached document), and information about the church.

- Pastor Bio: A section that introduces our pastor and gives a short bio about our pastor. Would like this section to include a picture of our pastor. Somewhere in this section I would like to include this Bible reference: "And I will give you pastors according to mine heart, which shall feed you with knowledge and understanding. Jer 3:15 KJV"

- Articles of Faith (What We Believe): This should include several sub-sections each with a heading, body, and possibly 1 or more scripture references. I have attached a document to the brief that includes our articles of faith. Feel free to be creative with this section in how you lay these out and format them.

- Support Us: A small section that explains what kind of support someone can give and a link to a donation page. The link can say something like "Support Us" or "Donate Now".

- Contact form: A contact form that allows the visitor to send us a message. The contact form should ask for name, email, phone, and message.

- Footer: A footer that will be displayed on all pages of the site. This should include at a minimum a link to the home page (or a link to each individual section in the home page if you prefer), a link to "listen live", a link to "support us", a link to "contact us" (or you can put the contact form directly in the footer if you prefer), the address, and a "member login" link.

Page 2: Support Us
The donation page should include a form the visitor can fill out to make a donation. We will embed a third party form later. For this design, please just mock out the design with a basic form asking for name, phone, and email.

Page 3: Login
The recording library (detailed below) will require members to login with a shared numeric code before accessing the page. We need a design for a login screen. The screen should include navigation/footer just like all other pages, but the body of the login page will consist only of a form that asks the user to enter the access code and then a "login" button.

Page 4: Recording Library

The library page is a member-only page that will require a shared, numeric pass code to access. On this page, members will be able to access a filterable list of past sermons. The page by default should display most recent sermons, but should also include a search form that allows the member to filter the sermon list to find a particular sermon. The search form should allow the user to select a filter type (e.g. Speaker name, date, event, etc.) and type in a value to search. They should be able to add multiple filters and remove filters that have been added. Each sermon that is displayed in the result list should include basic information such as title, date, speaker, tags, etc. along with a download icon, and an embedded audio player where they can click a play button to stream it on-demand. Each sermon should also have clickable tags associated with it that can be used to find related sermons.
Updates

Need extra days to review

I have uploaded several images of our church. Feel free to incorporate these into your design if possible.

Target Market(s)

Church Members

Industry/Entity Type

Religion

Number of Pages Required

4 page

Font styles to use
Sans Serif

Colors

Designer to choose colors to be used in the design.

Requirements
Must have
• Must incorporate the logo (attached)
Nice to have
• Would like the design to incorporate pictures of our church (attached) instead of stock photos if possible.
Should not have
• Please avoid an overly cluttered design. Stock photos used should not include any people in the photos.

```html
<!DOCTYPE html>
<html lang="en">
<head>
<meta charset="utf-8">
<title>Grace Covenant Church</title>
<link href="https://fonts.googleapis.com/css2?family=Cinzel:wght@400;500;700&family=Montserrat:ital,wght@0,400;0,500;0,600;1,400&display=swap" rel="stylesheet">
<style>
:root{
  --green:#86a86b;
  --blue:#4fb3d4;
  --navy:#4d6b88;
  --ink:#2f2f2f;
  --body:#666;
  --soft:#f6f4f4;
  --panel:#f4f4f4;
  --dark:#3a3a3a;
  --white:#fff;
}
*{margin:0;padding:0;box-sizing:border-box}
html,body{width:1200px;height:4622px;overflow:hidden}
body{position:relative;font-family:"Montserrat",sans-serif;color:var(--ink);background:var(--white)}
.abs{position:absolute}
.serif{font-family:"Cinzel",serif;font-weight:400}
.center{text-align:center;left:0;width:1200px}
p{font-size:13px;line-height:21px;color:var(--body)}
.btn{position:absolute;background:var(--green);color:#fff;font-family:"Cinzel",serif;font-size:14px;display:flex;align-items:center;justify-content:center;gap:8px;letter-spacing:.5px;text-decoration:none}
.btn i{width:16px;height:16px;border:1.5px solid #fff;border-radius:3px;display:inline-block}
.rule{position:absolute;height:3px;background:var(--navy)}
.eyebrow{font-size:13px;color:var(--blue);letter-spacing:1px}

/* header */
.brand{left:130px;top:20px;width:180px;text-align:center}
.brand-name{font-family:"Cinzel",serif;font-size:26px;color:var(--green);line-height:30px}
.brand-sq{width:30px;height:30px;border:2px solid var(--blue);margin:8px auto 10px}
.nav{top:52px;left:560px;display:flex;gap:48px;font-size:13px;color:var(--ink)}

/* hero */
.hero{top:150px;left:0;width:1200px;height:498px;background:linear-gradient(180deg,#f7f7f7 0%,#e9e4e1 40%,#b98e7a 62%,#9b7a68 80%,#d8d4d0 100%)}
.hero-title{top:190px;font-size:62px;letter-spacing:6px;color:var(--ink)}
.listen{left:488px;top:315px;width:194px;height:52px;border:1.5px solid var(--green);border-radius:30px;background:#f4f1ea;display:flex;align-items:center}
.listen b{width:52px;height:52px;border-radius:50%;background:var(--green);margin-left:-1px}
.listen span{font-family:"Cinzel",serif;color:var(--green);font-size:15px;margin-left:20px}

/* about */
.arch{left:158px;top:770px;width:318px;height:480px;border-radius:159px 159px 0 0;background:linear-gradient(160deg,#c9b3a0,#a7826c 50%,#8f6f5e)}
.about-text{left:572px;top:742px;width:450px}
.about-text h2{font-family:"Cinzel",serif;font-weight:400;font-size:35px;line-height:40px;letter-spacing:2px;margin:8px 0 14px}
.about-text p{margin-bottom:14px}
.times h3{font-family:"Cinzel",serif;font-size:17px;letter-spacing:1.5px;font-weight:500;margin:32px 0 14px}
.times li{list-style:none;font-family:"Cinzel",serif;font-size:13px;line-height:33px;letter-spacing:.5px}
.times li em{font-style:normal;color:var(--green);font-family:"Montserrat",sans-serif;font-size:11px;margin-right:8px}
.times li b{font-weight:700;margin-left:8px}

/* announcement */
.ann-box{left:180px;top:1372px;width:840px;height:300px;border:4px solid var(--navy);background:var(--panel)}
.ann-box::after{content:"";position:absolute;inset:8px;border:1px solid var(--navy)}
.ann-brand{left:530px;top:1320px;width:140px;background:var(--white);text-align:center;padding:6px 0 8px}
.ann-brand .sq{width:22px;height:22px;border:1.5px solid var(--blue);margin:0 auto 6px}
.ann-brand div+div{font-family:"Cinzel",serif;font-size:14px;line-height:17px;color:var(--green)}
.ann-title{top:1458px;font-size:34px;letter-spacing:3px}
.ann-copy{top:1505px;font-size:13px;line-height:22px;color:var(--ink)}

/* pastor */
.pastor{top:1686px;left:0;width:1200px;height:740px;background:linear-gradient(180deg,#fcfafa,#eeeaea 60%,#f6f4f4)}
.portrait{left:468px;top:1890px;width:264px;height:264px;border-radius:50%;border:6px solid #fff;box-shadow:0 0 0 1px #ccc;background:radial-gradient(circle at 50% 45%,#b89a86,#5e5654 60%,#3b3a3c)}
.quote{top:2246px;font-style:italic;font-size:17px;line-height:26px;color:#555}

/* articles */
.faith h4{font-family:"Cinzel",serif;font-weight:400;font-size:17px;letter-spacing:1.5px;line-height:22px;margin-bottom:12px;color:var(--ink)}
.faith h4::before{content:"•";color:var(--green);margin-right:8px}
.faith p{font-size:12px;line-height:20px}
.faith u{color:var(--ink);font-style:italic}
.faith ol{list-style:none;margin-top:10px}
.faith ol li{font-size:10px;line-height:23px;color:#555;font-style:italic;text-decoration:underline}
.faith ol li span{color:var(--green);font-style:normal;text-decoration:none;font-size:11px;margin-right:8px;display:inline-block}
.sep{height:1px;background:#ddd;width:210px;margin-top:22px}

/* support */
.support{top:3320px;left:0;width:1200px;height:410px;background:#f3f2f2}

/* contact */
.contact{top:3730px;left:0;width:1200px;height:892px;background:var(--dark)}
.field{position:absolute;border:1.5px solid #777;font-size:11px;color:#ddd;padding:14px 14px}
.foot{color:#ddd}
.foot p{color:#cfcfcf;font-size:12px;line-height:18px}
.links a{display:block;color:#ddd;font-size:13px;line-height:30px;text-decoration:none}
.social{top:4578px;left:928px;display:flex;gap:18px}
.social b{width:10px;height:10px;border-radius:50%;background:#fff}
</style>
</head>
<body>

<header>
  <div class="abs brand"><div class="brand-sq"></div><div class="brand-name">GRACE<br>COVENANT</div></div>
  <nav class="abs nav"><span>Home</span><span>Recording Library</span><span>Login</span></nav>
  <a class="btn" style="left:890px;top:40px;width:148px;height:42px"><i></i>SUPPORT US</a>
</header>

<section>
  <div class="abs hero" role="img" aria-label="Photo of the brick church building under a winter sky"></div>
  <h1 class="abs center serif hero-title" style="font-weight:400">KEEP FAITH ALWAYS</h1>
  <div class="rule" style="left:520px;top:278px;width:160px"></div>
  <div class="abs listen"><b></b><span>LISTEN LIVE</span></div>
</section>

<section>
  <svg class="abs" style="left:140px;top:680px" width="400" height="400" fill="none" stroke="#eee" stroke-width="3"><path d="M20 400V200A180 180 0 0 1 380 200V400"/><path d="M60 400V210A140 140 0 0 1 340 210V400"/></svg>
  <div class="abs arch" role="img" aria-label="Photo of the church front wall and sign"></div>
  <div class="abs about-text">
    <div class="eyebrow">ABOUT</div>
    <h2>WELCOME TO<br>GRACE COVENANT<br>CHURCH</h2>
    <p>Ut diam tortor consectetur lacus scelerisque tortor congue viverra egestas. Tristique in consectetur leo arcu blandit diam et sed volutpat.</p>
    <p>Aliquam at commodo venenatis quis. Velit neque interdum molestie risus consectetur vestibulum a eget. Ultricies volutpat orci eros quisque ullamcorper quis est.</p>
    <div class="rule" style="position:relative;width:150px;height:2px;background:var(--blue);margin-top:24px"></div>
    <div class="times">
      <h3>SERVICE TIME ARE</h3>
      <ul>
        <li><em>01.</em>WEDNESDAY EVENING SERVICE: <b>7:30 PM</b></li>
        <li><em>02.</em>SUNDAY SCHOOL: <b>10:00 AM</b></li>
        <li><em>03.</em>SUNDAY MORNING SERVICE: <b>11:00 AM</b></li>
        <li><em>04.</em>SUNDAY EVENING SERVICE: <b>5:30 PM</b></li>
      </ul>
    </div>
  </div>
</section>

<section>
  <div class="abs ann-box"></div>
  <div class="abs ann-brand"><div class="sq"></div><div>GRACE<br>COVENANT</div></div>
  <h2 class="abs center serif ann-title" style="font-weight:400">ANNOUNCEMENT BANNER SPOT</h2>
  <p class="abs center ann-copy">Ullamcorper facilisi egestas semper fames suscipit penatibus amet. Ut diam tortor<br>consectetur lacus scelerisque tortor congue viverra</p>
  <div class="abs serif" style="left:388px;top:1578px;font-size:17px;letter-spacing:2px">ANNOUNCEMENT</div>
  <div class="abs serif" style="left:470px;top:1612px;font-size:11px;letter-spacing:1px">FABRUARY 16TH</div>
  <div class="abs" style="left:592px;top:1572px;width:1.5px;height:56px;background:#555"></div>
  <div class="abs serif" style="left:616px;top:1576px;font-size:12px;line-height:15px;letter-spacing:1px">GRACE COVENANT<br>CHURCH</div>
  <div class="abs" style="left:616px;top:1610px;font-size:12px;font-style:italic">Pastor John Doe</div>
</section>

<section>
  <div class="abs pastor" role="img" aria-label="Soft blurred photo of the church sanctuary"></div>
  <div class="abs center eyebrow" style="top:1756px">OUR PASTOR</div>
  <h2 class="abs center serif" style="top:1780px;font-size:34px;line-height:42px;letter-spacing:2px;font-weight:400">A MAN OF PRAYER AND HIGH<br>SPIRITUALITY</h2>
  <div class="abs" style="left:170px;top:1920px;width:250px">
    <p>Ullamcorper facilisi egestas semper fames suscipit penatibus amet. Ut diam tortor consectetur lacus scelerisque tortor congue viverra egestas. Tristique in consectetur leo arcu blandit diam et sed volutpat.</p>
    <p style="margin-top:16px">Aliquam at commodo venenatis quis. Velit neque interdum molestie risus consectetur vestibulum a eget.</p>
  </div>
  <div class="abs portrait" role="img" aria-label="Portrait photo of the pastor holding a Bible"></div>
  <div class="abs center" style="top:2173px;font-size:8px;letter-spacing:1px">PASTOR</div>
  <div class="abs center serif" style="top:2186px;font-size:15px;font-weight:500">JOHN DOE</div>
  <div class="abs" style="left:768px;top:1920px;width:255px">
    <p>Ut diam tortor consectetur lacus scelerisque tortor congue viverra egestas. Tristique in consectetur leo arcu blandit diam et sed volutpat.</p>
    <p style="margin-top:16px">Aliquam at commodo venenatis quis. Velit neque interdum molestie risus consectetur vestibulum a eget.</p>
    <div class="serif" style="margin-top:28px;color:var(--green);font-size:13px;border-bottom:1px solid var(--green);display:inline-block;padding-bottom:6px">READ FULL BIO</div>
  </div>
  <p class="abs center quote">"And I will give you pastors according to mine heart, which shall feed<br>you with knowledge and understanding."</p>
  <div class="abs center serif" style="top:2322px;font-size:17px">JER 3:15 KJV</div>
</section>

<section class="faith">
  <h2 class="abs center serif" style="top:2518px;font-size:34px;letter-spacing:3px;font-weight:400">ARTICLES OF FAITH</h2>
  <div class="rule" style="left:510px;top:2572px;width:160px;background:var(--blue)"></div>

  <div class="abs" style="left:168px;top:2624px;width:245px">
    <h4>THE GOD HEAD.</h4>
    <p>We believe in the God head bodily, known as the Divine Trinity. This body consist of God the father, Jesus Christ, his only begotten son and the redeemer of the world, and of the Holy Ghost, The third person of the Divine Trinity</p>
    <div class="sep"></div>
  </div>
  <div class="abs" style="left:168px;top:2890px;width:245px">
    <h4>BAPTISM OF THE HOLY GHOST.</h4>
    <p>We believe in the baptism of the Holy Ghost as it is taught in the Bible and promised by our Lord Jesus Christ, with speaking in tongues as the Spirit gives utterance as the initial evidence. <u>Acts 2:4</u> we believe that the gift of the Holy Ghost is for all believers as the Lord promised. <u>Acts 2:17-18</u></p>
  </div>

  <div class="abs" style="left:463px;top:2624px;width:250px">
    <h4>FULL SALVATION.</h4>
    <p>We believe that Salvation is received only when a person comes to the realization that he or she is lost and separated from God and becomes full of godly sorrow, confessing their sins and true repentance, believing in the shed blood of the Lord Jesus Christ as the only sacrifice for sins. Through the blood of Christ we have:</p>
    <ol>
      <li><span>01.</span>Remission of sins, Matthew 26:28 Heb 9:22</li>
      <li><span>02.</span>Sanctification, Hebrews 13:12</li>
      <li><span>03.</span>Redemption, Revelations 5:9</li>
      <li><span>04.</span>Cleansing, 1 John 1:7 Rev. 1:5</li>
      <li><span>05.</span>Justification, Romans 5:9</li>
    </ol>
    <div class="sep"></div>
  </div>
  <div class="abs" style="left:463px;top:3045px;width:245px">
    <h4>SECOND COMING OF CHRIST.</h4>
    <p>We believe in the second coming of Jesus Christ. <u>Matthew 24:44 Luke 12:40</u></p>
    <div class="sep"></div>
  </div>

  <div class="abs" style="left:774px;top:2624px;width:245px">
    <h4>SANCTIFICATION</h4>
    <p>"Sanctify them through thy truth thy word is truth <u>St John 17:17</u>. For this is the will of God even your sanctification"</p>
    <p style="margin-top:12px">We believe in a set apart life, separate from the world to Christ <u>2 Cor 6:17-18</u></p>
  </div>
  <div class="abs" style="left:774px;top:2878px;width:245px">
    <h4>DIVINE HEALING.</h4>
    <p>We believe Divine Healing to be included in the atonement of Jesus Christ our Lord, And believe that it is still for us today. <u>1 Peter 2:24</u> <u>Luke 9:1-2 Mark 16-18 James 5:15</u></p>
    <div class="sep"></div>
  </div>
  <div class="abs" style="left:774px;top:3088px;width:245px">
    <h4>ETERNITY</h4>
    <p>We believe in Literal Eternity. Eternal Life for the believer and eternal death for those without Christ. <u>Revelations 21:1-27</u></p>
  </div>
</section>

<section>
  <div class="abs support" role="img" aria-label="Faint light-grey decorative background texture"></div>
  <div class="abs center" style="top:3436px;font-size:14px;letter-spacing:1.5px">SUPPORT US</div>
  <h2 class="abs center serif" style="top:3460px;font-size:34px;line-height:46px;letter-spacing:3px;font-weight:400">WHERE YOUR TREASURE IS, YOUR<br>HEART IS AS WELL</h2>
  <a class="btn" style="left:525px;top:3583px;width:148px;height:44px"><i></i>SUPPORT US</a>
</section>

<footer>
  <div class="abs contact" role="img" aria-label="Dark faded photo of the church building"></div>
  <div class="abs center serif" style="top:3820px;font-size:17px;color:#ddd;letter-spacing:2px">CONTACT US</div>
  <h2 class="abs center serif" style="top:3850px;font-size:34px;color:#fff;letter-spacing:3px;font-weight:400">FEEL FREE TO JOIN US</h2>
  <div class="field" style="left:176px;top:3913px;width:417px;height:44px">Name *</div>
  <div class="field" style="left:612px;top:3913px;width:412px;height:44px">Phone *</div>
  <div class="field" style="left:176px;top:3972px;width:848px;height:44px">Email address *</div>
  <div class="field" style="left:176px;top:4030px;width:848px;height:108px">Message</div>
  <a class="btn" style="left:536px;top:4155px;width:135px;height:46px;font-size:15px">SEND US →</a>

  <div class="abs foot" style="left:150px;top:4360px;width:300px;text-align:center">
    <div class="serif" style="font-size:15px;letter-spacing:1.5px;margin-bottom:12px">DONATION</div>
    <p>Aliquam at commodo venenatis quis. Velit<br>neque interdum molestie risus.</p>
  </div>
  <a class="btn" style="left:228px;top:4437px;width:149px;height:40px"><i></i>SUPPORT US</a>

  <div class="abs" style="left:590px;top:4360px;width:20px;height:20px;border:1.5px solid var(--blue)"></div>
  <div class="abs center serif" style="top:4400px;font-size:28px;line-height:34px;color:var(--green)">GRACE<br>COVENANT</div>

  <div class="abs foot" style="left:815px;top:4360px">
    <div class="serif" style="font-size:15px;letter-spacing:1.5px;margin-bottom:10px">QUICK LINKS</div>
    <div class="links"><a>Home</a><a>Recording Library</a><a>Contact Us</a><a>Login</a></div>
  </div>

  <div class="abs" style="left:0;top:4560px;width:1200px;height:1px;background:#555"></div>
  <div class="abs" style="left:98px;top:4578px;font-size:11px;color:#ddd">Copyright 2023 Grace Covenant Church I All rights reserved</div>
  <div class="abs social"><b></b><b></b><b></b><b></b></div>
</footer>

</body>
</html>
```